Transform this table

Please make a 2 page A4 handout from this boring table into an engaging design. The front page can be simple and engaging (a summary of the back where all the detail lives)

Target Market(s)

Business

Requirements
Must have
• Clarity. And impact.
Nice to have
• Icons

```html
<!DOCTYPE html>
<html lang="en">
<head>
<meta charset="utf-8">
<title>Safety Culture Maturity Ladder</title>
<link href="https://fonts.googleapis.com/css2?family=Varela+Round&family=Open+Sans:ital,wght@0,400;0,600;0,700;1,400&display=swap" rel="stylesheet">
<style>
  :root{
    --bg:#e8e8e8;
    --paper:#ffffff;
    --ink:#3a3f47;
    --muted:#4a4a4a;
    --panel:#f2f2f2;
    --red:#c00000; --red-head:#a30000; --red-top:#d51414; --red-side:#8a0000;
    --orange:#e2660f; --orange-head:#c6560b; --orange-top:#ec8326; --orange-side:#c04d08;
    --yellow:#fdc000; --yellow-head:#f0aa00; --yellow-top:#fde04e; --yellow-side:#d6a000;
    --lime:#8fd14f; --lime-head:#77c03a; --lime-top:#a6dc6a; --lime-side:#6bb02d;
    --green:#129440; --green-head:#0d7e36; --green-top:#1fb04e; --green-side:#0b6c2c;
    --brown:#5b3a00;
  }
  *{box-sizing:border-box;margin:0;padding:0}
  html,body{width:929px;height:1200px;overflow:hidden;background:var(--bg)}
  body{position:relative;font-family:"Open Sans",sans-serif;color:var(--muted)}
  .sheet{position:absolute;left:129px;width:1028px;height:730px;background:var(--paper);transform:scale(.652);transform-origin:0 0}
  .sheet--summary{top:87px}
  .sheet--detail{top:612px}
  .ladder{display:block;width:1028px;height:730px}
  .title{font-family:"Varela Round",sans-serif;font-size:34px;fill:var(--ink)}
  .title .strong{stroke:var(--ink);stroke-width:.9}
  .step-name{font-family:"Varela Round",sans-serif;font-size:21px;fill:#fff;text-anchor:middle;stroke:#fff;stroke-width:.4}
  .step-body{font-family:"Varela Round",sans-serif;font-size:16px;fill:#fff;text-anchor:middle;stroke:#fff;stroke-width:.3}
  .step-body--dark{fill:var(--brown);stroke:var(--brown)}
  .trend{font-family:"Varela Round",sans-serif;fill:var(--ink);text-anchor:middle}
  .note{font-family:"Open Sans",sans-serif;font-style:italic;font-size:13.5px;fill:var(--ink)}
  .credit{font-family:"Open Sans",sans-serif;font-style:italic;font-size:14px;fill:var(--ink);text-anchor:end}
  .arrow-line{fill:none;stroke:var(--ink);stroke-width:2}

  .columns{position:absolute;left:65px;top:52px;display:flex;gap:7px}
  .col{width:174px;height:626px;display:flex;flex-direction:column}
  .col__bar{height:8px}
  .col__body{flex:1;background:var(--panel);padding:12px 5px 0 6px;font-size:10.8px;line-height:15px;color:#3d3d3d}
  .col__band{display:flex;align-items:center;justify-content:center;color:#fff;font-family:"Varela Round",sans-serif;font-size:18px;font-weight:700;letter-spacing:.3px}
  .col ul{list-style:none}
  .col li{position:relative;padding-left:11px}
  .col li::before{content:"•";position:absolute;left:0}
  .col li ul{margin-left:1px}
  .col h4{font-size:12px;font-weight:700;text-align:center;margin:14px 0 12px;line-height:17px}
  .col strong{font-weight:700}
  .col--vulnerable .col__bar,.col--vulnerable .col__band{background:var(--red)}
  .col--reactive .col__bar,.col--reactive .col__band{background:var(--orange)}
  .col--compliant .col__bar,.col--compliant .col__band{background:var(--yellow)}
  .col--proactive .col__bar,.col--proactive .col__band{background:var(--lime)}
  .col--resilient .col__bar,.col--resilient .col__band{background:var(--green)}
</style>
</head>
<body>

<section class="sheet sheet--summary">
  <svg class="ladder" viewBox="0 0 1028 730" xmlns="http://www.w3.org/2000/svg">
    <text class="title" x="70" y="80"><tspan class="strong">Safety</tspan> Culture</text>
    <text class="title" x="70" y="117"><tspan class="strong">Maturity Ladder</tspan></text>
    <rect x="70" y="137" width="31" height="3" fill="var(--orange)"/>
    <rect x="101" y="137" width="32" height="3" fill="var(--yellow)"/>
    <rect x="133" y="137" width="32" height="3" fill="var(--green)"/>

    <line x1="159" y1="297" x2="740" y2="107" stroke="var(--ink)" stroke-width="2"/>
    <polygon points="747,104 733,103 737,114" fill="var(--ink)"/>
    <text class="trend" font-size="19" transform="translate(437,177) rotate(-18)">Improving safety culture</text>
    <text class="trend" font-size="16" transform="translate(456,230) rotate(-18)">Increasing accountability &amp; reliability</text>

    <!-- Vulnerable -->
    <polygon points="70,412 223,412 263,375 110,375" fill="var(--red-top)"/>
    <polygon points="223,412 263,375 263,556 223,593" fill="var(--red-side)"/>
    <rect x="70" y="412" width="153" height="181" fill="var(--red)"/>
    <rect x="70" y="412" width="153" height="45" fill="var(--red-head)"/>
    <text class="step-name" x="143" y="441">Vulnerable</text>
    <text class="step-body" x="146" y="497">Toxic /</text>
    <text class="step-body" x="146" y="514">No care culture</text>
    <text class="step-body" x="146" y="531">“accidents</text>
    <text class="step-body" x="146" y="549">happen”</text>

    <!-- Reactive -->
    <polygon points="242,355 395,355 435,318 282,318" fill="var(--orange-top)"/>
    <polygon points="395,355 435,318 435,500 395,537" fill="var(--orange-side)"/>
    <rect x="242" y="355" width="153" height="182" fill="var(--orange)"/>
    <rect x="242" y="355" width="153" height="47" fill="var(--orange-head)"/>
    <text class="step-name" x="314" y="384">Reactive</text>
    <text class="step-body" x="318" y="449">Blame Culture</text>
    <text class="step-body" x="318" y="466">“it was</text>
    <text class="step-body" x="318" y="483">an accident!”</text>

    <!-- Compliant -->
    <polygon points="413,299 566,299 606,262 453,262" fill="var(--yellow-top)"/>
    <polygon points="566,299 606,262 606,444 566,481" fill="var(--yellow-side)"/>
    <rect x="413" y="299" width="153" height="182" fill="var(--yellow)"/>
    <rect x="413" y="299" width="153" height="47" fill="var(--yellow-head)"/>
    <text class="step-name" x="491" y="328">Compliant</text>
    <text class="step-body step-body--dark" x="485" y="390">Compliance</text>
    <text class="step-body step-body--dark" x="485" y="407">Culture</text>
    <text class="step-body step-body--dark" x="485" y="424">“Incidents</text>
    <text class="step-body step-body--dark" x="485" y="441">have causes”</text>

    <!-- Proactive -->
    <polygon points="584,242 737,242 777,205 624,205" fill="var(--lime-top)"/>
    <polygon points="737,242 777,205 777,388 737,425" fill="var(--lime-side)"/>
    <rect x="584" y="242" width="153" height="183" fill="var(--lime)"/>
    <rect x="584" y="242" width="153" height="47" fill="var(--lime-head)"/>
    <text class="step-name" x="659" y="273">Proactive</text>
    <text class="step-body" x="665" y="331">Ownership</text>
    <text class="step-body" x="665" y="348">Culture</text>
    <text class="step-body" x="665" y="365">“We prevent</text>
    <text class="step-body" x="665" y="382">incidents”</text>

    <!-- Resilient -->
    <polygon points="756,185 909,185 949,148 796,148" fill="var(--green-top)"/>
    <polygon points="909,185 949,148 949,332 909,369" fill="var(--green-side)"/>
    <rect x="756" y="185" width="153" height="184" fill="var(--green)"/>
    <rect x="756" y="185" width="153" height="48" fill="var(--green-head)"/>
    <text class="step-name" x="829" y="214">Resilient</text>
    <text class="step-body" x="835" y="277">Interdependent</text>
    <text class="step-body" x="835" y="294">culture</text>
    <text class="step-body" x="835" y="311">“It’s how</text>
    <text class="step-body" x="835" y="328">we do business.”</text>

    <!-- Step arrows -->
    <path class="arrow-line" d="M145 645 H282 Q292 645 292 635 V590"/>
    <polygon points="292,580 287,591 297,591" fill="var(--ink)"/>
    <text class="note" x="311" y="611">Wake</text>
    <text class="note" x="311" y="626">management &amp; control</text>
    <text class="note" x="311" y="641">high risks</text>

    <path class="arrow-line" d="M318 585 H454 Q464 585 464 575 V530"/>
    <polygon points="464,520 459,531 469,531" fill="var(--ink)"/>
    <text class="note" x="484" y="553">Standardise</text>
    <text class="note" x="484" y="568">processes &amp; gain</text>
    <text class="note" x="484" y="583">commitment</text>

    <path class="arrow-line" d="M489 526 H628 Q638 526 638 516 V471"/>
    <polygon points="638,461 633,472 643,472" fill="var(--ink)"/>
    <text class="note" x="666" y="495">All team members</text>
    <text class="note" x="666" y="510">engaged &amp; all risks</text>
    <text class="note" x="666" y="525">controlled</text>

    <path class="arrow-line" d="M664 466 H802 Q812 466 812 456 V411"/>
    <polygon points="812,401 807,412 817,412" fill="var(--ink)"/>
    <text class="note" x="834" y="433">Develop</text>
    <text class="note" x="834" y="448">consistency &amp; fight</text>
    <text class="note" x="834" y="463">complacency</text>

    <text class="credit" x="948" y="643">Based on the</text>
    <text class="credit" x="948" y="659">Harlow Institute and Daniel Marsh</text>
    <text class="credit" x="948" y="675">“<tspan font-weight="700">steps and stages</tspan>” model</text>
  </svg>
</section>

<section class="sheet sheet--detail">
  <div class="columns">
    <article class="col col--vulnerable">
      <div class="col__bar"></div>
      <div class="col__body">
        <ul>
          <li><strong>Toxic / No care culture</strong>
            <ul><li>Apathy / resistance</li><li>Near misses not considered</li><li>Negligence</li><li>Dishonesty</li><li>Hiding of incidents</li><li>Serious injury/health risks are unseen or ignored</li><li>Unfair disciplinary actions</li></ul></li>
          <li>No or little training</li>
          <li>Poor or no communication</li>
          <li>Production at almost any cost</li>
          <li>“Just get it done” attitude or blatantly unsafe</li>
        </ul>
        <h4>Accept that incidents happen</h4>
        <ul>
          <li>Reactive or unresponsive approach</li><li>No OHS systems</li><li>No risk assessment</li><li>Legal non compliance</li><li>Accept equipment / process decay</li><li>Only fix when broken / unsafe repairs</li><li>Reports are shelved / used irresponsibly</li><li>No or poor investigation</li><li>No monitoring / audits</li><li>Permit non-compliance</li><li>Potential illegal practices</li>
        </ul>
      </div>
      <div class="col__band" style="height:42px">Vulnerable</div>
    </article>

    <article class="col col--reactive">
      <div class="col__bar"></div>
      <div class="col__body">
        <ul>
          <li><strong>Blame culture</strong>
            <ul><li>Dependent on natural instincts</li><li>Accept need to care</li><li>Some near miss reporting</li><li>Some window dressing e.g. pre-inspection cleanups and light duty</li><li>Disciplinary action</li></ul></li>
          <li>Minimum / inconsistent training</li>
          <li>Some communication on a need to know basis</li>
        </ul>
        <h4>Prevent a similar incident</h4>
        <ul>
          <li>Administrator driven</li><li>Loose systems, elements of an OHS Management System</li><li><strong>Reactive risk assessment and control</strong></li><li>Minimum legal compliance</li><li>Apply PPE as a way of eliminating exposure</li>
          <li><strong>Incident investigation but limited analysis</strong>
            <ul><li>Focus on what happened</li><li>No systems focus</li><li>Human faults occur</li></ul></li>
          <li>Ad hoc monitoring / audits</li><li>No occupational hygiene or health initiatives</li><li>Reactive medical monitoring</li><li>Monitoring as per regulations</li>
        </ul>
      </div>
      <div class="col__band" style="height:56px">Reactive</div>
    </article>

    <article class="col col--compliant">
      <div class="col__bar"></div>
      <div class="col__body">
        <ul>
          <li><strong>Compliance culture</strong>
            <ul><li>Supervision dependent</li><li>Some participation</li><li>Near miss discussions</li></ul></li>
          <li>Acceptable training / awareness</li>
          <li>Established and good communication channels</li>
          <li>Regular people involvement and focus</li>
        </ul>
        <h4>Prevent incidents before they occur</h4>
        <ul>
          <li>OHS coordinator driven</li><li>OHS standards system and ISO 9002 or equivalent</li><li><strong>Risk assessment through existing systems</strong></li><li>Total legal compliance goal</li><li>Strictly enforced the use of PPE where required (knowing risk)</li><li><strong>Causal incident analysis based on events potential</strong></li><li>Info sharing from events</li><li>Planned occupational hygiene / environmental monitoring</li><li>Periodical medical examinations</li><li><strong>Planned monitoring / audits</strong></li><li>Safety meetings and talks</li><li>Some task observations</li>
        </ul>
      </div>
      <div class="col__band" style="height:70px">Compliant</div>
    </article>

    <article class="col col--proactive">
      <div class="col__bar"></div>
      <div class="col__body">
        <ul>
          <li><strong>Independent &amp; personal ownership culture</strong>
            <ul><li>Involvement at all levels</li><li>Near miss involvement</li></ul></li>
          <li>High level of training / awareness</li>
          <li>Communication at a high level hiding nothing</li>
        </ul>
        <h4>Improve the systems</h4>
        <ul>
          <li>Committed leadership at all levels</li><li>Line driven systems improvement</li><li>ISO 14001 and ISO 45001</li><li><strong>Pro-active formal risk management</strong></li><li>Beyond legal compliance</li><li>Seek to actively engineer out process / equipment inadequacies</li><li><strong>Incident learnings shared with all levels</strong></li><li>Well designed plans / procedures</li><li><strong>Focus on adhering to site plans and procedures</strong></li><li>Integrated audits</li><li>Peer evaluations and discussion</li>
        </ul>
      </div>
      <div class="col__band" style="height:85px">Proactive</div>
    </article>

    <article class="col col--resilient">
      <div class="col__bar"></div>
      <div class="col__body">
        <ul>
          <li><strong>Interdependent teams culture</strong></li>
          <li>Way of life
            <ul><li>Comes natural</li><li>Personal involvement by all to manage risks well and prevent incidents</li><li>Authentic communication throughout culture</li></ul></li>
        </ul>
        <h4>Way we do business</h4>
        <ul>
          <li>Individually internalized</li><li>Inspiring genuine leadership</li><li>No silo thinking or actions</li><li>All staff active, positive, respected, speaking up</li><li>Excellent equipment, ultra-organised</li><li>Integrated management systems</li><li><strong>Risk management cycle integrated into all systems</strong></li><li>Self regulating style</li><li><strong>Eliminate &amp; prevent problems before they occur</strong></li><li>All threats considered in decision-making</li><li><strong>Continually improving through external evaluation / auditing</strong></li><li>Multiple positive performance indicators drive PDCA cycle</li>
        </ul>
      </div>
      <div class="col__band" style="height:99px">Resilient</div>
    </article>
  </div>
</section>

</body>
</html>
```